Pomme Sauvage Riding School Flyer Design

We need a flyer for our Horse riding school, called Pomme Sauvage Riding School.

At Pomme Sauvage Riding School, Horses and ponies are carefully matched to suit each rider's experience, ability and confidence. I am a Qualified instructor, equipped to train all levels from nervous beginners to the more advanced.

Horse riding is fun! Riders, particularly children, are taught not only skills on the horse, but skills that are integral to good horsemanship and ownership of horses.

We regularly host Ladies Days, Guest Instructors, 1 hour Trail Rides and Pony Ride Days!

We teach people how to interact safely with, and care for horses so they develop a genuine love and respect for the animals and the sport.

In addition to fundamental riding techniques including walk, trot, and canter, we teach our students:
Grooming and Care of horses, Safety around horses, Balance and Co-Ordination, How to saddle up and care for Tack, Responsibility for equipment and horse, Confidence and Confidence Building for all Ages.

Private and group lessons start at 5 years of age upwards.

We recommend children 4 years and under partake in 15 minute pony rides, mainly due to their attention span!

```html
<!DOCTYPE html>
<html lang="en">
<head>
<meta charset="utf-8">
<title>Pomme Sauvage Riding School Flyer</title>
<link href="https://fonts.googleapis.com/css2?family=Arimo:wght@400;700&family=Roboto:wght@400;500&family=Delius&display=swap" rel="stylesheet">
<style>
  :root {
    --page-bg: #e4e4e4;
    --panel-left: #3f4a3f;
    --panel-right: #363a33;
    --strip: #444c43;
    --lime: #c8dc2a;
    --white: #ffffff;
    --muted: #5e6458;
    --sky-top: #7fb0e0;
    --sky-mid: #e6eff8;
    --grass: #5f9a2e;
  }
  * { margin: 0; padding: 0; box-sizing: border-box; }
  html, body { width: 1200px; height: 1000px; overflow: hidden; }
  body { background: var(--page-bg); font-family: "Arimo", Arial, sans-serif; position: relative; }

  .flyer {
    position: absolute; left: 70px; top: 110px;
    width: 1058px; height: 750px; overflow: hidden;
  }
  .flyer-shapes { position: absolute; inset: 0; }

  .brand {
    position: absolute; left: 0; top: 0; width: 390px; height: 750px;
    color: var(--white); text-align: center;
  }
  .brand-mark {
    position: absolute; left: 155px; top: 395px; width: 70px; height: 70px;
    border: 2px solid var(--white); border-radius: 50%;
  }
  .brand-name {
    position: absolute; left: 0; width: 390px; top: 543px;
    font-family: "Roboto", sans-serif; font-weight: 500;
    font-size: 30px; letter-spacing: 3px; white-space: nowrap;
  }
  .brand-sub {
    position: absolute; left: 0; width: 390px; top: 592px;
    font-family: "Roboto", sans-serif; font-weight: 500;
    font-size: 18px; letter-spacing: 4px;
  }
  .brand-location {
    position: absolute; left: 28px; top: 638px;
    font-family: "Delius", cursive; font-size: 19px; color: var(--lime);
  }
  .brand-phone {
    position: absolute; left: 34px; top: 686px;
    font-weight: 700; font-size: 37px; letter-spacing: 7px; white-space: nowrap;
  }

  .pitch { position: absolute; right: 20px; left: 380px; color: var(--white); text-align: right; }
  .pitch-intro { top: 440px; font-size: 19px; color: var(--lime); text-align: left; left: 382px; }
  .pitch-headline { top: 468px; font-size: 24px; font-weight: 700; text-align: left; left: 397px; }
  .pitch-levels { top: 500px; font-size: 21px; font-weight: 700; color: var(--lime); letter-spacing: 1.3px; }
  .pitch-body { top: 548px; font-size: 17px; line-height: 21.5px; }
  .pitch-offer { top: 635px; font-size: 20px; font-weight: 700; color: var(--lime); }
  .pitch-note { top: 673px; font-size: 14px; font-weight: 700; color: var(--muted); }
  .pitch-extras { top: 703px; font-size: 17px; letter-spacing: 0.2px; }
</style>
</head>
<body>
  <main class="flyer">
    <svg class="flyer-shapes" width="1058" height="750" viewBox="0 0 1058 750">
      <defs>
        <linearGradient id="photoTones" x1="0" y1="0" x2="0" y2="1">
          <stop offset="0" stop-color="var(--sky-top)"/>
          <stop offset="0.45" stop-color="var(--sky-mid)"/>
          <stop offset="0.7" stop-color="#a8c878"/>
          <stop offset="1" stop-color="var(--grass)"/>
        </linearGradient>
      </defs>
      <rect class="hero-photo" x="0" y="0" width="1058" height="460" fill="url(#photoTones)" role="img" aria-label="Photo of two chestnut horses galloping across a grassy meadow under a blue cloudy sky"/>
      <path class="info-panel" d="M330,420 Q640,370 1058,445 L1058,750 L330,750 Z" fill="var(--panel-right)"/>
      <path class="info-edge" d="M330,420 Q640,370 1058,445" fill="none" stroke="var(--lime)" stroke-width="3"/>
      <rect class="extras-strip" x="330" y="693" width="728" height="57" fill="var(--strip)"/>
      <path class="brand-panel" d="M0,275 C240,275 380,380 395,750 L0,750 Z" fill="var(--panel-left)" stroke="var(--white)" stroke-width="3"/>
    </svg>

    <section class="brand">
      <div class="brand-mark"></div>
      <div class="brand-name">POMME SAUVAGE</div>
      <div class="brand-sub">RIDING SCHOOL</div>
      <div class="brand-location">Find us at Orchard Rd, Willowvale</div>
      <div class="brand-phone">0400 555 218</div>
    </section>

    <section>
      <p class="pitch pitch-intro">At Pomme Sauvage Riding School,</p>
      <h1 class="pitch pitch-headline">OUR QUALIFIED INSTRUCTORS TUTOR</h1>
      <h2 class="pitch pitch-levels">ALL LEVELS OF EXPERIENCE AND CONFIDENCE</h2>
      <p class="pitch pitch-body">Horses and ponies are carefully matched to each rider's ability allowing<br>us to teach people how to interact safely with and care for horses and<br>nurturing a genuine love and respect for the animals and the sport</p>
      <p class="pitch pitch-offer">PRIVATE, GROUP LESSONS AND TRAIL RIDES AVAILABLE</p>
      <p class="pitch pitch-note">ALL AGES ARE CATERED FOR. ALL EQUIPMENT AND INSURANCE PROVIDED</p>
      <p class="pitch pitch-extras">Ask about Ladies Days, Guest Instructors, Trail Rides and Pony Rides</p>
    </section>
  </main>
</body>
</html>
```